Wordpress Theme for Cedarline Clinics

** Please view updated Sitemap2.pdf doc to clarify some confusion ***

This is a multiuser WordPress subscription site for Cedarline Clinics. Please see attachment for sitemap. Please do not include extra content like social media icons, search bars, or images. If you have questions, please ask for clarification.
The site contains the following pages and sub-pages:

1. Home
2. Our Clinic
2a. Our Clinic > Mission
2b. Our Clinic > Services
2c. Our Clinic > Clinic Policies
2d. Our Clinic > Schedules
3. Our Staff
3a. Our Staff > [Staff member page]
4. Resources
4a. Resources > Patient Health (index)
4b. Resources > Patient Health (index) > [post]
4c. Resources > Links
4d. Resources > Forms
5. Alerts
5a. Alerts > [Alert Page]
6. Contact Us

Includes the Following Pages, Subpages, and Content
1. Home
a. About Us
b. Our Staff
c. Bulletins
d. Accepting New Patients (shown as an alert widget)
e. Links
i. Physician Toolbox
ii. Book an Appointment
f. Clinic Policies
i. Show first 3 policies (e.g. Late Arrivals, Missed Appointments, Fees)
ii. Link to Clinic Policies page
g. Primary widget (displayed on all pages)
i. Hours of operation
ii. Contact Info
1. Tel
2. Fax
3. Email
4. Address
5. Get directions (link to Google Maps)
2. Our Clinic
a. Main Page
i. Clinic Name
ii. Overview
iii. Languages Spoken
iv. Secondary Navigation
1. Mission
2. Services
3. Clinic Policies
4. Schedules (see attachment)
b. Our Clinic > Mission
c. Our Clinic > Services
i. For each service include service TITLE and DESCRIPTION
d. Our Clinic > Clinic Policies
i. For each policy include policy TITLE and DESCRIPTION
ii. Include the following policies in mockup
1. Late arrivals
2. Missed appointments
3. Fees for missed appointments
4. Referrals and follow-ups
5. Services not covered by RDV
6. Information for TQL patients
7. Medical Legal Reports
e. Our Clinic > Schedules
3. Our Staff
a. Main Page
i. Display a list of staff members. Include NAME and DESIGNATION
b. Our Staff > [Staff Name]
i. Include NAME, PICTURE, DESIGNATION, and BIO
4. Resources
a. Resources > Patient Health
i. Main Page
1. Posts (ordered by date)
a. Title
b. Summary
2. Side Navigation
a. Post Categories
ii. Patient Health > [post title]
1. Title
2. Post Category
3. Date
4. Author
5. Summary
6. Body
b. Resources > Links
1. Secondary Navigation - Categories
a. Sample Categories:
i. Local Services
ii. RDV and Drug Coverage
iii. Mental Health Resources
2. Category page
a. Include the following links in the 'Local Services' category
i. Hypertension clinics
ii. Home Care services
iii. Vaccine Clinics
c. Resources > Forms
i. Display a table with form TITLE and CATEGORY
ii. Side Navigation
1. Form Categories
a. Use the following sample Categories
i. Referrals
ii. Insurance
iii. Intake
iv. Discharge
v. Waivers
5. Alerts
a. Main page
i. List of all Alert posts
1. Include post TITLE as a link to the post
ii. Side Navigation
1. Alerts Archive
a. shown as Month + Number of posts
iii. Alerts > [Alert page]
1. Include TITLE, DATE, AUTHOR, BODY
6. Contact Us
a. Map
b. Hours of operation
c. Address
d. Phone number
e. Fax number
e. Fax number
f. Map
g. Email

Design notes:
- fixed width
- responsive (need designs for mobile, tablet, and desktop)
- simple, dark font, white background
- use Font Awesome icons where needed
- user adds own logo

Target Market(s)

Cedarline Clinics

Industry/Entity Type

Medical

Number of Pages Required

5+ page

Font styles to use
Serif
Sans Serif

Requirements
Must have
• Please keep designs very simple.
• Examples:
• https://www.quandrix.com/install
• http://www.tervolane.com/company/about-us
• http://brightnumberhub.org/
• http://www.vorn.com/
Should not have
• Minimal or no use of shadows and gradients

```html
<!DOCTYPE html>
<html lang="en">
<head>
<meta charset="utf-8">
<title>Cedarline Clinics – Patient Health</title>
<link href="https://fonts.googleapis.com/css2?family=Open+Sans:wght@400;600;700&display=swap" rel="stylesheet">
<style>
:root{
  --blue:#0a8ce0;
  --blue-dark:#0a74cc;
  --ink:#2b2b2b;
  --text:#333333;
  --muted:#777777;
  --line:#d9d9d9;
  --band:#f7f7f7;
  --footer:#262626;
  --footer-text:#8a8a8a;
  --white:#ffffff;
}
*{box-sizing:border-box;margin:0;padding:0}
html,body{width:1200px;height:1035px;overflow:hidden}
body{font-family:"Open Sans",Arial,sans-serif;color:var(--text);background:var(--white);position:relative}
a{color:inherit;text-decoration:none}
ul{list-style:none}

.topbar{position:absolute;left:0;top:0;width:1200px;height:30px;background:var(--blue);color:var(--white);font-size:9.5px}
.topbar .help{position:absolute;left:161px;top:9px}
.topbar .help span+span{border-left:1px solid var(--white);margin-left:4px;padding-left:4px}
.topbar .quick{position:absolute;right:161px;top:9px}
.topbar .quick a+a{border-left:1px solid var(--white);margin-left:4px;padding-left:5px}

.masthead{position:absolute;left:0;top:30px;width:1200px;height:83px}
.brand{position:absolute;left:162px;top:26px;display:flex;align-items:center;gap:12px}
.brand-dot{width:26px;height:26px;border-radius:50%;background:var(--blue)}
.brand-name{font-size:20px;font-weight:600;color:var(--ink)}
.main-nav{position:absolute;left:0;top:0;height:83px;font-size:11px;color:var(--ink)}
.main-nav a{position:absolute;top:0;height:83px;line-height:83px;text-align:center}
.main-nav a.active{background:var(--blue-dark);color:var(--white)}

.pagehead{position:absolute;left:0;top:113px;width:1200px;height:59px;background:var(--band)}
.pagehead h1{position:absolute;left:162px;top:15px;font-size:10.5px;font-weight:600;color:var(--ink)}
.pagehead .crumbs{position:absolute;left:162px;top:34px;font-size:9.5px;color:var(--ink)}

.article{position:absolute;left:161px;top:218px;width:652px}
.article .section{font-size:10.5px;font-weight:600;color:var(--ink);padding-bottom:7px;border-bottom:1px solid var(--line)}
.article h2{font-size:12.5px;font-weight:700;color:var(--ink);line-height:17px;margin-top:17px;padding-bottom:12px;border-bottom:1px solid var(--line)}
.article .meta{font-size:9px;color:var(--muted);margin-top:9px}
.article .meta b{font-weight:400;color:var(--ink)}
.article .meta span{margin-right:14px}
.article p{font-size:9.5px;line-height:15px;margin-top:15px;text-align:justify}
.article p.lead{font-weight:700;margin-top:11px;color:var(--ink)}

.widget{position:absolute;left:836px;width:203px;border:1px solid var(--line);background:var(--white)}
.widget h3{height:33px;line-height:33px;background:var(--blue);color:var(--white);font-size:10.5px;font-weight:700;padding-left:13px}
.cats{top:210px;height:150px;padding-bottom:10px}
.cats ul{padding:12px 17px 0 14px;font-size:9.5px}
.cats li{display:flex;justify-content:space-between;height:18px}
.cats li.current{color:var(--blue-dark)}
.hours{top:381px;height:361px}
.hours .intro{font-size:9.5px;line-height:13px;padding:10px 14px 0;color:var(--ink)}
.hours dl{display:grid;grid-template-columns:90px 1fr;font-size:9.5px;padding:10px 14px 0;row-gap:0}
.hours dl dt,.hours dl dd{height:18px}
.hours hr{border:0;border-top:1px solid var(--line);margin:19px 14px 0}
.hours h4{font-size:10.5px;font-weight:700;padding:14px 14px 0;color:var(--ink)}
.contact{display:grid;grid-template-columns:93px 1fr;font-size:9.5px;line-height:15px;padding:6px 14px 0}

.footer{position:absolute;left:0;top:808px;width:1200px;height:227px;background:var(--footer);border-top:4px solid var(--blue)}
.footer .brand{left:162px;top:40px}
.footer .brand-name{color:var(--white)}
.footer .about{position:absolute;left:162px;top:89px;width:205px;font-size:8.5px;line-height:13px;color:#d8d8d8}
.fcol{position:absolute;top:36px;font-size:9.5px;color:var(--footer-text)}
.fcol h5{font-size:12.5px;font-weight:600;color:#9a9a9a;margin-bottom:8px}
.fcol li{height:18px}
.fcol li.current{color:#cfcfcf}
.fcol .contact{padding:0 0 0 2px;grid-template-columns:89px 1fr;color:var(--footer-text)}
.bottom{position:absolute;left:0;top:188px;width:1200px;height:35px;border-top:1px solid #444;font-size:9.5px;color:var(--footer-text)}
.bottom .copy{position:absolute;left:162px;top:10px}
.bottom nav a{position:absolute;top:10px}
</style>
</head>
<body>

<header>
  <div class="topbar">
    <div class="help"><span>To help Here : 555 010 2233</span><span>Email : contact@cedarline.ca</span></div>
    <div class="quick"><a href="#">Book an Appointment</a><a href="#">Physician Toolbox</a></div>
  </div>
  <div class="masthead">
    <a class="brand" href="#"><span class="brand-dot"></span><span class="brand-name">Cedarline Clinics</span></a>
    <nav class="main-nav">
      <a href="#" style="left:560px;width:50px">Home</a>
      <a href="#" style="left:632px;width:62px">Our Clinic</a>
      <a href="#" style="left:718px;width:58px">Our Staff</a>
      <a href="#" class="active" style="left:803px;width:60px">Resources</a>
      <a href="#" style="left:890px;width:42px">Alerts</a>
      <a href="#" style="left:958px;width:62px">Contact Us</a>
    </nav>
  </div>
</header>

<section class="pagehead">
  <h1>RESOURCES</h1>
  <div class="crumbs">HOME / RESOURCES/PATIENT-HEALTH</div>
</section>

<main class="article">
  <div class="section">PATIENT HEALTH</div>
  <h2>Lorem Ipsum is simply dummy text of the printing and typesetting industry. Lorem Ipsum has been the industry's standard dummy</h2>
  <div class="meta"><span>Author : <b>admin</b></span><span>24-June-2015</span><span>Category : <b>Local Services</b></span></div>
  <p class="lead">Contrary to popular belief, Lorem Ipsum is not simply random text. It has roots in a piece of classical Latin literature from 45 BC, making it over 2000 years old. Arthur Pellman, a Latin professor at Halvern College in Virginia, looked up one of the more obscure Latin words, consectetur, from a Lorem Ipsum passage, and going through the cites of the word in classical literature,</p>
  <p>Lorem Ipsum is simply dummy text of the printing and typesetting industry. Lorem Ipsum has been the industry's standard dummy text ever since the 1500s, when an unknown printer took a galley of type and scrambled it to make a type specimen book. It has survived not only five centuries, but also the leap into electronic typesetting, remaining essentially unchanged.</p>
  <p>It was popularised in the 1960s with the release of Typeline sheets containing Lorem Ipsum passages, and more recently with desktop publishing software like Setwell PageForm including versions of Lorem Ipsum.There are many variations of passages of Lorem Ipsum available, but the majority have suffered alteration in some form, by injected humour, or randomised words which don't look even slightly believable.</p>
  <p>College in Virginia, looked up one of the more obscure Latin words, consectetur, from a Lorem Ipsum passage, and going through the cites of the word in classical literature, discovered the undoubtable source. Lorem Ipsum comes from sections 1.10.32 and 1.10.33 of "de Finibus Bonorum et Malorum" (The Extremes of Good and Evil) by Severan Maro, written in 45 BC. This book is a treatise on the theory of ethics, very popular during the Renaissance. The first line of Lorem Ipsum, "Lorem ipsum dolor sit amet..", comes from a line in section 1.10.32.</p>
  <p>Discovered the undoubtable source. Lorem Ipsum comes from sections 1.10.32 and 1.10.33 of "de Finibus Bonorum et Malorum" (The Extremes of Good and Evil) by Severan Maro, written in 45 BC. This book is a treatise on the theory of ethics, very popular during the Renaissance. The first line of Lorem Ipsum, "Lorem ipsum dolor sit amet..", comes from a line in section 1.10.32.</p>
  <p>College in Virginia, looked up one of the more obscure Latin words, consectetur, from a Lorem Ipsum passage, and going through the cites of the word in classical literature, discovered the undoubtable source. Lorem Ipsum comes from sections 1.10.32 and 1.10.33 of "de Finibus Bonorum et Malorum" (The Extremes of Good and Evil) by Severan Maro, written in 45 BC. This book is a treatise on the theory of ethics, very popular during the Renaissance. The first line of Lorem Ipsum, "Lorem ipsum dolor sit amet..", comes from a line in section 1.10.32.</p>
</main>

<aside>
  <div class="widget cats">
    <h3>CATEGORIES</h3>
    <ul>
      <li><span>Referrals</span><span>(8)</span></li>
      <li class="current"><span>Insurance</span><span>(20)</span></li>
      <li><span>Intake</span><span>(5)</span></li>
      <li><span>Discharge</span><span>(9)</span></li>
      <li><span>Waivers</span><span>(35)</span></li>
    </ul>
  </div>
  <div class="widget hours">
    <h3>HOURS OF OPRATION</h3>
    <div class="intro">Lorem Ipsum is simply dummy text of the printing and typesetting</div>
    <dl>
      <dt>Monday :</dt><dd>8:00 AM - 6:00 PM</dd>
      <dt>Tuesday :</dt><dd>8:00 AM - 6:00 PM</dd>
      <dt>Wednesday :</dt><dd>8:00 AM - 6:00 PM</dd>
      <dt>Thursday :</dt><dd>8:00 AM - 6:00 PM</dd>
      <dt>Friday :</dt><dd>8:00 AM - 6:00 PM</dd>
      <dt>Saturday :</dt><dd>9:00 AM - 4:00 PM</dd>
      <dt>Sunday :</dt><dd>9:00 AM - 4:00 PM</dd>
    </dl>
    <hr>
    <h4>CONTACT INFO</h4>
    <div class="contact">
      <span>Telephone :</span><span>604-555-0190</span>
      <span>Email:</span><span>contact@cedarline.ca</span>
      <span>Address:</span><span>45 Harbour Lane<br>Alderton,<br>Canada, K2P 4RT</span>
    </div>
  </div>
</aside>

<footer class="footer">
  <a class="brand" href="#"><span class="brand-dot"></span><span class="brand-name">Cedarline Clinics</span></a>
  <p class="about">Lorem Ipsum is simply dummy text of the printing and typesetting industry. Lorem Ipsum has been the industry's standard dummy text</p>
  <div class="fcol" style="left:461px">
    <h5>Navigation</h5>
    <ul><li class="current">Home</li><li>Our Clinic</li><li>Newsletter</li><li>Our Staff</li><li>Resources</li></ul>
  </div>
  <div class="fcol" style="left:686px">
    <h5>Links</h5>
    <ul><li>Help</li><li>Support</li><li>Privacy Policy</li></ul>
  </div>
  <div class="fcol" style="left:836px">
    <h5>Contact Us</h5>
    <div class="contact">
      <span>Telephone :</span><span>604-555-0190</span>
      <span>Email:</span><span>contact@cedarline.ca</span>
      <span>Address:</span><span>45 Harbour Lane<br>Alderton, Canada,<br>K2P 4RT</span>
    </div>
  </div>
  <div class="bottom">
    <span class="copy">© 2015 Cedarline Clinics. All Rights Reserved</span>
    <nav>
      <a href="#" style="left:463px">About Us</a>
      <a href="#" style="left:530px">Terms of Use</a>
      <a href="#" style="left:615px">Privacy Policy</a>
    </nav>
  </div>
</footer>

</body>
</html>
```